AMAZING WEBSITE DESIGN NEEDED FOR MAID / CLEANING SERVICE

NOTE: This is Website Design Only - No coding required

Please submit your designs ASAP as we want to pick a winner and get started!

Hey,

We are looking for a new amazing website design for a maid or cleaning service.

They have a horrible website that we want turned into a masterpiece.

As you will see on their current site:

http://tidyharborco.examplehost.net/

They have a lot of stuff, very disorganized, and need help.

Here is what we need:

Colors: Same as current site, Orange, Gray, Black

Menu: Horizontal with same Menu items

Need a spot for a video on the homepage

Want content to be structured in a great format that is easy to read.

Want to highlight commercial and residential on the website homepage.

Also want a spot for customer testimonials

We want the site clean, professional, fresh and modern.

Please help by matching the logo design.

I look forward to your designs!
Updates

Hi All! Really appreciate your efforts and designs. I will be meeting with our client on Monday and will then be able to provide feedback after our meeting. If you have other ideas, please submit them. The more I can show him the better! Thanks!

Target Market(s)

The target market is residential home owners as well as commercial businesses who need cleaning on a regular basis.

This company cleans homes and offices for individuals.

Industry/Entity Type

Residential

Font styles to use
Sans Serif

Requirements
Must have
• Must match logo colors
Must have spot for video
Must have a clean look
Must have a bold look
Nice to have
• Highly visual
Should not have
• clutter
messy design
hard to read

```html
<!DOCTYPE html>
<html lang="en">
<head>
<meta charset="utf-8">
<title>Tidy Harbor – Our Speciality</title>
<link href="https://fonts.googleapis.com/css2?family=Arimo:wght@400;700&family=Cabin:wght@400;500&family=Alfa+Slab+One&display=swap" rel="stylesheet">
<style>
:root{
  --orange:#f7a51c;
  --orange-deep:#f38b00;
  --orange-text:#f47b14;
  --heading-gray:#4a4a4a;
  --body-gray:#3d3d3d;
  --card:#565656;
  --footer:#1b1b1b;
  --white:#ffffff;
}
*{margin:0;padding:0;box-sizing:border-box}
html,body{width:1200px;height:1155px;overflow:hidden;background:var(--white)}
body{position:relative;font-family:'Arimo',Arial,sans-serif}

.section-title{position:absolute;left:95px;top:14px;font:700 31px/1 'Arimo',Arial,sans-serif;letter-spacing:1.5px;color:var(--heading-gray)}
.section-title span{color:var(--orange-text)}

.speciality-band{position:absolute;left:0;top:67px;width:1200px;height:291px;
  background:linear-gradient(#e6e6e6 0,#fafafa 14%,#fff 50%,#f7f7f7 86%,#e6e6e6 100%);
  -webkit-mask:linear-gradient(90deg,transparent,#000 6%,#000 94%,transparent);
  mask:linear-gradient(90deg,transparent,#000 6%,#000 94%,transparent)}
.speciality{position:absolute;top:94px;width:220px;text-align:center}
.speciality .badge{width:148px;height:148px;margin:0 auto;border-radius:50%;border:3px solid #e4e4e4;box-shadow:0 2px 6px rgba(0,0,0,.15)}
.speciality p{margin-top:14px;font:400 14.5px/18px 'Cabin',sans-serif;color:var(--body-gray)}
.badge.eco{background:radial-gradient(circle at 45% 55%,#5cb82e 0,#2e8a2a 45%,#f4f8f0 47%,#ffffff 100%)}
.badge.family{background:linear-gradient(160deg,#6fb9e6 0,#d9b89a 40%,#8c6a55 75%,#e8e2dc 100%)}
.badge.ribbon{background:radial-gradient(circle,#f7a8cf 0,#f29bc7 100%)}
.badge.seal{border:none;background:radial-gradient(circle,#c8841a 0,#9e5a0c 55%,#d9a233 70%,#8a4f0a 100%)}

.bid-bar{position:absolute;left:93px;top:380px;width:997px;height:79px;background:var(--orange)}
.bid-bar svg{position:absolute;left:0;top:0}
.bid-label{position:absolute;left:17px;top:20px;font:400 33px/1 'Alfa Slab One',serif;color:var(--white);letter-spacing:1px}
.bid-copy{position:absolute;left:380px;right:30px;top:13px;text-align:center;font:400 20.5px/24px 'Cabin',sans-serif;color:#2b2b2b}

.testimonials-title{position:absolute;left:0;width:1185px;top:494px;text-align:center;font:700 29px/1 'Arimo',Arial,sans-serif;color:var(--orange-text)}
.testimonials-sub{position:absolute;left:0;width:1185px;top:532px;text-align:center;font:400 18px/1 'Cabin',sans-serif;color:#4d4d4d}

.card{position:absolute;top:638px;width:228px;height:344px;background:var(--card);border-radius:7px;box-shadow:3px 4px 6px rgba(0,0,0,.3)}
.card .avatar{position:absolute;left:55px;top:-59px;width:118px;height:118px;border-radius:50%;border:3px solid #fff;background:#fff;display:flex;align-items:center;justify-content:center;box-shadow:0 1px 3px rgba(0,0,0,.25)}
.avatar.photo-a{background:radial-gradient(circle at 50% 45%,#d79a7e 0,#a4472c 55%,#5e1f12 100%)}
.avatar.photo-b{background:radial-gradient(circle at 50% 45%,#e2bfa8 0,#8a6a58 50%,#1e1e22 100%)}
.studio-name{font:700 14px/1.1 'Arimo',sans-serif;color:#1b78c2;text-align:center}
.card blockquote{position:absolute;left:16px;right:16px;top:90px;height:168px;overflow:hidden;text-align:center;font:400 14.5px/24px 'Arimo',Arial,sans-serif;color:var(--white)}
.card cite{position:absolute;left:0;right:0;top:272px;text-align:center;font:400 14.5px/1 'Arimo',Arial,sans-serif;font-style:normal;color:var(--orange)}

.site-footer{position:absolute;left:0;top:1049px;width:1200px;height:106px;background:var(--footer)}
.footer-nav{position:absolute;left:111px;top:32px;font:400 14.5px/1 'Cabin',sans-serif;color:#e8e8e8}
.footer-nav a{color:#e8e8e8;text-decoration:none}
.footer-nav a.current{color:var(--orange)}
.footer-nav .sep{margin:0 7px}
.copyright{position:absolute;left:111px;top:60px;font:400 14.5px/1 'Cabin',sans-serif;color:#e8e8e8}
.social{position:absolute;left:871px;top:1082px;display:flex;gap:14px}
.social span{width:28px;height:28px;display:block}
</style>
</head>
<body>

<h2 class="section-title">OUR <span>SPECIALITY</span></h2>
<div class="speciality-band"></div>

<div class="speciality" style="left:82px">
  <div class="badge eco" role="img" aria-label="Eco friendly globe emblem"></div>
  <p>Tidy Harbor is commited to using Eco Green chemicals to keep you and your family safe!</p>
</div>
<div class="speciality" style="left:343px">
  <div class="badge family" role="img" aria-label="Photo of a family relaxing at home"></div>
  <p>Proudly serving our amazing customers in the Albuquerque Metro &amp; surrounding areas!</p>
</div>
<div class="speciality" style="left:601px">
  <div class="badge ribbon" role="img" aria-label="Pink awareness ribbon"></div>
  <p>Tidy Harbor proudly donates 1% of its earnings to find a cure for breast cancer!</p>
</div>
<div class="speciality" style="left:857px">
  <div class="badge seal" role="img" aria-label="Satisfaction guarantee seal"></div>
  <p>We guarantee you will be 100% satisfied with our cleaning and our cleaning professionals!</p>
</div>

<div class="bid-bar">
  <svg width="997" height="79" viewBox="0 0 997 79" aria-hidden="true">
    <polygon points="0,0 316,0 346,39.5 316,79 0,79" fill="var(--orange-deep)"/>
    <polyline points="316,0 346,39.5 316,79" fill="none" stroke="#fff" stroke-width="9"/>
    <polygon points="338,0 352,0 382,39.5 352,79 338,79 368,39.5" fill="#fff"/>
  </svg>
  <div class="bid-label">REQUEST A BID</div>
  <div class="bid-copy">Locally Owned &amp; Operated<br>Never deal with an unresponsive franchise - Deal with the owner!</div>
</div>

<h2 class="testimonials-title">TESTIMONIALS</h2>
<p class="testimonials-sub">see what our clients says</p>

<div class="card" style="left:98px">
  <div class="avatar"><span class="studio-name">Brightline<br>Studio</span></div>
  <blockquote>I was very impressed with the amount they do for the price! Remarkable! Thank you Tidy Harbor for taking this daily headache away from my fiance. She was so thrilled. See you guys again soon! -</blockquote>
  <cite>Owen Carlisle</cite>
</div>
<div class="card" style="left:352px">
  <div class="avatar photo-a" role="img" aria-label="Client portrait photo"></div>
  <blockquote>hank you Tidy Harbor for making my house so fresh and clean! How nice it was to have all of my laundry washed and folded and my dishes done and put away along with everything else! Celia was so pleasant to</blockquote>
  <cite>Marlene Ashcroft</cite>
</div>
<div class="card" style="left:606px">
  <div class="avatar"><span class="studio-name">Brightline<br>Studio</span></div>
  <blockquote>I was very impressed with the amount they do for the price! Remarkable! Thank you Tidy Harbor for taking this daily headache away from my fiance. She was so thrilled. See you guys again soon! -</blockquote>
  <cite>Owen Carlisle</cite>
</div>
<div class="card" style="left:860px">
  <div class="avatar photo-b" role="img" aria-label="Client portrait photo"></div>
  <blockquote>"I was very happy with the cleaning. Our maid Greta was so nice and even took the time to wash my dog Milo (which I hate givnig my dog a bath) Im sure Milo does not like Greta anymore, casue Milo hate baths</blockquote>
  <cite>Joanne Pruitt</cite>
</div>

<footer class="site-footer">
  <nav class="footer-nav">
    <a class="current" href="#">Home</a><span class="sep">|</span><a href="#">About Us</a><span class="sep">|</span><a href="#">Services</a><span class="sep">|</span><a href="#">Why Choose Us?</a><span class="sep">|</span><a href="#">Request A Bid</a><span class="sep">|</span><a href="#">Contact Us</a>
  </nav>
  <p class="copyright">© 2014, All Rights Reserved, Tidy Harbor</p>
</footer>
<div class="social" aria-label="Social links">
  <span style="background:#3b5a98" role="img" aria-label="Social link one"></span>
  <span style="background:#3f8fd2" role="img" aria-label="Social link two"></span>
  <span style="background:#d2412f" role="img" aria-label="Social link three"></span>
  <span style="background:#c8281d" role="img" aria-label="Social link four"></span>
  <span style="background:#f26a1b" role="img" aria-label="Feed link"></span>
</div>

</body>
</html>
```